依頼詳細
『コンサルティングのご案内』という冊子を作りたいと思ってます。
原稿はこちらで作成しております。また、会社のロゴもありますので、シンプルなデザインを組み合わせていただいて、上品で高品質な印象を持ってもらえるような冊子ができたらいいなと思っております。
記載項目
①表紙は『コンサルティングのご案内』という文章とデザイン
②③は原稿がありますので、それにシンプルなデザインを組み合わせ
④ロゴとシンプルなデザイン

イメージは上記のような感じですが、絶対ではありませんので、デザイナーさんのセンスにお任せいたします。
サイズ
A4
ページ数
4ページ
希望イメージ
シンプル 複雑
単色 カラフル
暗い 明るい
日常 高級
遊び心 厳粛
未来的 伝統的
女性的 男性的
希望する色
紙で高級感を出そうと思っておりますので、白がベースかなと思っております。
補足説明
PDFでの納品が希望です。
納品物は作成いただいたデータでもお願いします。
追記です。

会社案内の冊子は別にありますので、会社案内的な要素を入れる必要はありません。

新たに『コンサルティングのご案内』、という別冊子を作る趣旨は、そこだけを取り上げた冊子を作りたいからです。

デザインも会社案内的な特徴を出すために少し派手な印象を入れる、というのとは真逆で、むしろ少し控えめにするくらいで、本当にシンプルでワンポイント的なデザインの方がいいです。

イメージとしては、高級フレンチ料理のメニュー表、とか、結婚式のメニュー表、のようなそんな感じの冊子ができればいいと思っております。

よろしくお願いいたします。
■ 選んだ理由

最も趣旨を汲んでくださった提案でしたので、選出させていただきました。

シンプルの中にも、高級感と奥深さを感じられ、ただの紙にとどまらず、全体のデザインから、質の高いコンサルティングを受けることができそうだと、思っていただけるような、デザインからそういった力を感じさせることができるような、素晴らしいデザインだったと思います。

■ 提案者全員のお礼・コメント

この度は、ご多忙にもかかわらず、たくさんの方にご提案をいただきまして、誠にありがとうございました。
素晴らしい提案がとても多く、非常に贅沢な悩みで、選出させていただきました。
このような形でしか御礼をお伝えすることができず、心苦しい点もありますが、気にかけていただき、そして、お時間を使っていただき、ご提案いただきましたことに、心から感謝申し上げます。
またぜひ次の機会にご縁をいただければ、大変嬉しく思います。
ありがとうございました。

```html
<!DOCTYPE html>
<html lang="ja">
<head>
<meta charset="utf-8">
<title>コンサルティングのご案内</title>
<link rel="stylesheet" href="https://fonts.googleapis.com/css2?family=Shippori+Mincho:wght@400;500;600&display=swap">
<style>
  :root {
    --paper: #ffffff;
    --ink: #3c3c3c;
    --ink-soft: #6a6a6a;
    --crimson: #9e1b32;
    --crimson-deep: #7a0f22;
    --gold: #c6a46a;
    --gold-soft: #e4d3b2;
    --rule: #d9d9d9;
  }
  * { margin: 0; padding: 0; box-sizing: border-box; }
  html, body { width: 1200px; height: 849px; overflow: hidden; background: var(--paper); }
  body { font-family: "Shippori Mincho", "Noto Serif JP", serif; color: var(--ink); }
  .spread { position: relative; width: 1200px; height: 849px; background: var(--paper); }
  .page { position: absolute; top: 0; width: 600px; height: 849px; }
  .page--left { left: 0; }
  .page--right { left: 600px; }
  .curves { position: absolute; inset: 0; }

  .section-title { position: absolute; font-size: 15px; letter-spacing: 0.12em; font-weight: 500; display: flex; align-items: center; gap: 8px; }
  .section-title::before { content: ""; width: 7px; height: 7px; background: currentColor; }
  .section-title--crimson { color: var(--crimson); left: 62px; top: 40px; }
  .section-title--gold { color: var(--gold); left: 155px; top: 40px; }
  .section-title span { color: var(--ink); }
  .subtitle { position: absolute; left: 66px; top: 62px; font-size: 8px; color: var(--ink-soft); letter-spacing: 0.06em; }

  .lead { position: absolute; left: 110px; top: 143px; font-size: 13.5px; line-height: 1.65; color: var(--crimson); font-weight: 600; letter-spacing: 0.06em; }
  .body-copy { position: absolute; left: 110px; top: 195px; width: 340px; font-size: 7.5px; line-height: 2; color: var(--ink-soft); }
  .body-copy p + p { margin-top: 12px; }

  .note-box { position: absolute; left: 58px; top: 610px; width: 200px; font-size: 6.8px; line-height: 1.9; color: var(--ink-soft); }
  .note-box h3 { font-size: 7px; color: var(--crimson); font-weight: 500; margin-bottom: 3px; }
  .note-box ul { list-style: none; }
  .note-box li::before { content: "□ "; }
  .note-box .indent { padding-left: 34px; }
  .note-box .caption { margin-top: 10px; font-size: 5.8px; }

  .flow { position: absolute; left: 90px; top: 72px; width: 300px; list-style: none; }
  .flow li { display: grid; grid-template-columns: 22px 1fr; margin-bottom: 14px; }
  .flow .num { color: var(--gold); font-size: 13px; font-weight: 600; line-height: 1.2; }
  .flow h4 { color: var(--gold); font-size: 11px; font-weight: 600; letter-spacing: 0.08em; border-bottom: 1px dotted var(--gold-soft); padding-bottom: 2px; width: 130px; }
  .flow p { font-size: 6.8px; line-height: 1.9; color: var(--ink-soft); margin-top: 3px; }
  .flow .aside { padding-left: 12px; font-size: 6.2px; }
</style>
</head>
<body>
<main class="spread">
  <section class="page page--left">
    <svg class="curves" width="600" height="849" viewBox="0 0 600 849" aria-hidden="true">
      <path d="M178 0 C 120 40, 60 90, 0 120" fill="none" stroke="var(--crimson)" stroke-width="1.4"/>
      <path d="M0 430 C 30 560, 42 700, 40 849" fill="none" stroke="var(--crimson)" stroke-width="1.2"/>
      <path d="M262 849 C 300 760, 370 690, 600 640 L600 660 C 390 705, 320 770, 300 849 Z" fill="var(--crimson-deep)"/>
      <path d="M470 0 C 560 150, 590 330, 580 520" fill="none" stroke="var(--rule)" stroke-width="1"/>
    </svg>
    <h2 class="section-title section-title--crimson"><span>コンサルティングのご案内</span></h2>
    <p class="subtitle">〜各社それぞれの状況に応じた具体的なコンサルティングを実施させていただきます〜</p>
    <p class="lead">最適な対策内容を検討し、<br>ご提案書を作成させていただきます。</p>
    <div class="body-copy">
      <p>提案書作成までの流れとしては、資料一式をご提出いただきまして、財務分析、株価算定を実施し、対策の方向性の打合せを行わせていただき、提案書を作成させていただきます。</p>
      <p>また、資料の提出及び財務分析等については専門スタッフが担当し、ご要望、ご希望に沿うかたちで、コンサルティングの流れを丁寧に確認し、対策案作成までを一貫して担当させていただきます。</p>
      <p>さらに、提案書をご覧いただいたうえでのご質問やご相談にも、<br>コンサルタントがご質問に応じて、個別に丁寧にご説明いたします。<br>提案書ご送付後のフォローも承ります。</p>
    </div>
    <div class="note-box">
      <h3>■ ご提案に必要な資料のご案内</h3>
      <ul>
        <li>株主名簿（株主構成がわかるもの）</li>
        <li>決算報告書（三期分）</li>
      </ul>
      <p class="indent">・勘定科目内訳書<br>・固定資産台帳</p>
      <p>（内容）　・登記簿謄本、附属明細書</p>
      <p class="indent">・不動産の評価資料</p>
      <ul><li>その他、ご状況に応じた資料</li></ul>
      <p class="caption">※ご提出いただいた資料は厳重に管理し、目的外には使用いたしません。</p>
    </div>
  </section>

  <section class="page page--right">
    <svg class="curves" width="600" height="849" viewBox="0 0 600 849" aria-hidden="true">
      <path d="M250 0 C 420 40, 560 160, 600 300" fill="none" stroke="var(--gold)" stroke-width="1.4"/>
      <path d="M20 849 C 120 760, 260 740, 430 700 C 500 680, 560 640, 600 600" fill="none" stroke="var(--gold)" stroke-width="1.2"/>
      <path d="M0 60 C 40 260, 50 520, 0 760" fill="none" stroke="var(--rule)" stroke-width="1"/>
    </svg>
    <h2 class="section-title section-title--gold"><span>コンサルティングのながれ</span></h2>
    <ol class="flow">
      <li><span class="num">1</span><div><h4>個別面談（無料）</h4><p>ご来社いただき、ご要望、課題等をお伺いいたします。</p></div></li>
      <li><span class="num">2</span><div><h4>資料のご提出</h4><p>必要資料一式をご提出いただきます。</p></div></li>
      <li><span class="num">3</span><div><h4>財務分析・株価算定</h4><p>資料をもとに財務分析・株価算定を実施いたします。</p></div></li>
      <li><span class="num">4</span><div><h4>対策の方向性の打合せ</h4><p>財務分析と株価算定の結果をもとに、対策の方向性について打合せをいたします。</p></div></li>
      <li><span class="num">5</span><div><h4>提案書の作成</h4><p>打合せ内容を踏まえ提案書を作成し、ご説明いたします。</p></div></li>
      <li><span class="num">6</span><div><h4>対策実行</h4><p>提案内容にご同意いただいた後、対策を実行いたします。</p><p class="aside">・スケジュールの管理<br>・関係各所との調整</p></div></li>
      <li><span class="num">7</span><div><h4>対策完了</h4><p>対策完了後、結果をご報告いたします。</p></div></li>
      <li><span class="num">8</span><div><h4>メンテナンス</h4><p>対策完了後も定期的にフォローいたします。</p></div></li>
    </ol>
  </section>
</main>
</body>
</html>
```